Presentation Folder

We are looking for a design for a presentation folder given to clients upon first meeting.

Requirements
Must have
• Corporate contact information on one of the interior sleeves. Must use company logo. Full color interior and exterior. Should have similar feel to business cards and envelopes (see attached samples). If you have trouble with the template files for the folder size, you can visit this site (it is the last option on the page): http://zelvaro.net/g/showStaticPage.do?page=download_templates-pres.html

```html
<!DOCTYPE html>
<html lang="en">
<head>
<meta charset="utf-8">
<title>Birch Hollow Realty – Presentation Folder</title>
<link rel="stylesheet" href="https://fonts.googleapis.com/css2?family=Cinzel:wght@400;500&family=Roboto+Condensed:wght@300&display=swap">
<style>
  :root {
    --page: #ffffff;
    --maroon-deep: #4a1a1c;
    --maroon-mid: #7a4345;
    --maroon-light: #b36767;
    --brand: #8b3f40;
    --ghost: #efe4e3;
    --silver-dark: #4d4d4f;
    --silver-light: #e4e4e6;
    --fold: #9a9a9a;
    --address: #dcbcbc;
    --web: #8a8a8a;
    --caption: #111111;
  }
  html, body {
    margin: 0;
    padding: 0;
    width: 1200px;
    height: 1000px;
    overflow: hidden;
    background: var(--page);
  }
  .folder-canvas {
    display: block;
    width: 1200px;
    height: 1000px;
  }
  .panel { fill: var(--page); }
  .panel-shadow { filter: drop-shadow(0 1px 3px rgba(0,0,0,0.35)); }
  .ghost-circle { fill: var(--ghost); }
  .fold-line {
    stroke: var(--fold);
    stroke-width: 1;
    stroke-dasharray: 4 3;
    fill: none;
  }
  .slit { stroke: #2a1012; stroke-width: 1.2; }
  .brand-mark { fill: var(--brand); }
  .brand-name {
    font-family: "Cinzel", serif;
    font-weight: 500;
    fill: var(--brand);
    text-anchor: middle;
  }
  .brand-name--primary { font-size: 30px; letter-spacing: 0.5px; }
  .brand-name--secondary { font-size: 17px; letter-spacing: 5px; }
  .web-address {
    font-family: "Cinzel", serif;
    font-size: 13px;
    fill: var(--web);
    text-anchor: middle;
    letter-spacing: 0.6px;
  }
  .street-address {
    font-family: "Cinzel", serif;
    font-size: 17px;
    fill: var(--address);
    letter-spacing: 1px;
  }
  .sheet-caption {
    font-family: "Roboto Condensed", sans-serif;
    font-weight: 300;
    font-size: 36px;
    fill: var(--caption);
    text-anchor: end;
  }
</style>
</head>
<body>
<svg class="folder-canvas" viewBox="0 0 1200 1000" xmlns="http://www.w3.org/2000/svg">
  <defs>
    <linearGradient id="maroon-fade" gradientUnits="userSpaceOnUse" x1="0" y1="560" x2="0" y2="935">
      <stop offset="0" stop-color="var(--maroon-deep)"/>
      <stop offset="0.45" stop-color="var(--maroon-mid)"/>
      <stop offset="0.75" stop-color="var(--maroon-light)"/>
      <stop offset="1" stop-color="var(--maroon-light)"/>
    </linearGradient>
    <linearGradient id="silver-left" x1="0" y1="0" x2="1" y2="0">
      <stop offset="0" stop-color="var(--silver-dark)"/>
      <stop offset="0.45" stop-color="var(--silver-light)"/>
      <stop offset="1" stop-color="var(--silver-dark)"/>
    </linearGradient>
    <linearGradient id="silver-right" x1="1" y1="0" x2="0" y2="0">
      <stop offset="0" stop-color="var(--silver-dark)"/>
      <stop offset="0.45" stop-color="var(--silver-light)"/>
      <stop offset="1" stop-color="var(--silver-dark)"/>
    </linearGradient>
  </defs>

  <!-- Folder sheet -->
  <g class="panel-shadow">
    <rect class="panel" x="104" y="58" width="986" height="660"/>
    <path class="pocket pocket--left" fill="url(#maroon-fade)"
          d="M62,730 L104,716 L597,716 L581,918 Q579,935 562,935 L104,935 L62,926 Z"/>
    <path class="pocket pocket--right" fill="url(#maroon-fade)"
          d="M600,716 L1090,716 L1132,730 L1132,926 L1090,935 L638,935 Q620,935 618,918 Z"/>
  </g>

  <!-- Back cover -->
  <g class="back-cover">
    <circle class="ghost-circle" cx="435" cy="410" r="80"/>
    <path class="swoosh" fill="url(#silver-left)"
          d="M104,460 Q330,560 597,562 Q350,588 104,538 Z"/>
    <path class="band" fill="url(#maroon-fade)"
          d="M104,552 Q370,632 597,566 L597,716 L104,716 Z"/>
    <text class="street-address" x="145" y="671">482 Alder Lane, Fenwick, Maryland 21290</text>
  </g>

  <!-- Front cover -->
  <g class="front-cover">
    <circle class="brand-mark" cx="917" cy="170" r="14"/>
    <text class="brand-name brand-name--primary" x="917" y="240">Birch Hollow</text>
    <text class="brand-name brand-name--secondary" x="917" y="262">Realty</text>
    <text class="web-address" x="917" y="289">www.HarborHomeFinder.com</text>
    <path class="swoosh" fill="url(#silver-right)"
          d="M1090,470 Q880,560 600,562 Q850,588 1090,535 Z"/>
    <path class="band" fill="url(#maroon-fade)"
          d="M600,566 Q850,628 1090,548 L1090,716 L600,716 Z"/>
  </g>

  <!-- Die lines -->
  <line class="fold-line" x1="597" y1="58" x2="597" y2="716"/>
  <line class="fold-line" x1="104" y1="735" x2="104" y2="935"/>
  <line class="slit" x1="423" y1="767" x2="450" y2="795"/>
  <line class="slit" x1="250" y1="857" x2="277" y2="885"/>

  <text class="sheet-caption" x="1182" y="980">Front/back of folder</text>
</svg>
</body>
</html>
```